2018 PLVWA Conference Theme Artwork

We need artwork designed around the theme of this year's human resources conference. The theme is "Celebrating 20 Years Together Towards Tomorrow". The artwork should be designed as a 4x6 postcard and will eventually be adapted/reformatted to use on the registration website, sales materials, e-newsletters, conference guide cover and signage.

Target Market(s)

Attendees are human resources professionals. Exhibitors and sponsors are companies who want to sell their products/services to human resource professionals

Colors

Designer to choose colors to be used in the design.

Requirements
Must have
• NO BORING PIXBANQ IMAGERY PLEASE.
• Theme: Celebrating 20 Years Together Towards Tomorrow
• Event: 20th Annual PLVW Conference
• Dates/Times: Tuesday, May 15, 2018, 12:30pm - 5:00pm and Wednesday, May 16, 2018 7:30am - 5:30pm
• Website: plvwsummit.example
• Location: The HALL at the Corvane Manchester
Nice to have
• Engaging, celebratory, visually attractive
Should not have
• NO BORING PIXBANQ IMAGERY.

```html
<!DOCTYPE html>
<html lang="en">
<head>
<meta charset="utf-8">
<title>PLVWA 2018 Conference Postcard</title>
<link rel="stylesheet" href="https://fonts.googleapis.com/css2?family=Anton&family=Oswald:wght@700&family=Montserrat:wght@400;700;800&display=swap">
<style>
  :root {
    --page-bg: #e6e7e9;
    --navy: #1c2738;
    --navy-deep: #121a27;
    --red: #b3131c;
    --blue: #143e79;
    --maroon: #6a0f12;
    --band-grey: #3a3b3d;
    --white: #ffffff;
  }
  * { margin: 0; padding: 0; box-sizing: border-box; }
  html, body {
    width: 1200px; height: 902px; overflow: hidden;
    background: var(--page-bg);
    font-family: "Montserrat", sans-serif;
  }
  .postcard {
    position: absolute; left: 0; top: 51px;
    width: 1200px; height: 800px;
    background: linear-gradient(90deg, var(--navy-deep) 0%, var(--navy) 55%, #1d2a3d 100%);
    overflow: hidden;
  }
  .hero-photo {
    position: absolute; left: 0; top: 0; width: 640px; height: 721px;
    background:
      radial-gradient(ellipse at 44% 46%, rgba(120,180,220,0.55) 0%, rgba(60,110,150,0.25) 22%, transparent 40%),
      radial-gradient(ellipse at 40% 64%, rgba(214,150,120,0.55) 0%, transparent 30%),
      linear-gradient(90deg, #141c28 0%, #26354a 45%, #1a2434 80%, rgba(28,39,56,0) 100%);
  }
  .client-name {
    position: absolute; left: 140px; top: 48px;
    font-family: "Montserrat", sans-serif; font-weight: 800;
    font-size: 64px; letter-spacing: 2px;
    color: rgba(20,50,90,0.75);
  }
  .headline { position: absolute; left: 0; top: 0; width: 1200px; height: 721px; }
  .rule {
    position: absolute; left: 713px; width: 365px;
    border-top: 1.5px dashed rgba(255,255,255,0.55);
  }
  .event-banner {
    position: absolute; left: 589px; top: 445px; height: 59px; width: 611px;
    display: flex; font-weight: 700; font-size: 30px; color: var(--white);
  }
  .event-banner .edition {
    width: 253px; background: var(--blue); border-radius: 4px 0 0 4px;
    display: flex; align-items: center; justify-content: center;
  }
  .event-banner .event-name {
    flex: 1; background: var(--red);
    display: flex; align-items: center; padding-left: 12px;
  }
  .event-date { position: absolute; top: 552px; width: 245px; height: 160px; color: var(--white); }
  .event-date .date-art { position: absolute; left: 0; top: 0; overflow: visible; }
  .event-date .time {
    position: absolute; left: 4px; top: 132px;
    font-weight: 700; font-size: 25px; letter-spacing: 0.5px; white-space: nowrap;
  }
  .date-joiner {
    position: absolute; left: 857px; top: 601px; width: 50px; height: 50px;
    border-radius: 50%; background: var(--blue); color: var(--white);
    font-weight: 700; font-size: 28px;
    display: flex; align-items: center; justify-content: center;
  }
  .info-band { position: absolute; left: 0; top: 721px; width: 1200px; height: 60px; }
  .info-band .band-shape { position: absolute; left: 0; top: 0; }
  .venue, .website {
    position: absolute; top: 0; height: 60px;
    display: flex; align-items: center; gap: 12px;
    color: var(--white); font-weight: 700; font-size: 28px; white-space: nowrap;
  }
  .venue svg, .website svg { flex: none; display: block; }
  .venue { left: 38px; }
  .website { left: 730px; }
  .card-foot {
    position: absolute; left: 0; top: 781px; width: 1200px; height: 19px;
    background: linear-gradient(#ffffff, #e4e4e4);
  }
</style>
</head>
<body>
<main class="postcard">
  <div class="hero-photo" role="img" aria-label="Photo of a businessman's cupped hands holding glowing figures of a team of people"></div>
  <div class="client-name">PLVWA</div>

  <svg class="headline" viewBox="0 0 1200 721" aria-label="Celebrating 20 Years Together Towards Tomorrow">
    <defs>
      <linearGradient id="silverFill" x1="0" y1="0" x2="0" y2="1">
        <stop offset="0" stop-color="#f2f4f6"/>
        <stop offset="0.5" stop-color="#c9ced4"/>
        <stop offset="1" stop-color="#9aa1aa"/>
      </linearGradient>
      <linearGradient id="redFill" x1="0" y1="0" x2="0" y2="1">
        <stop offset="0" stop-color="#e0301f"/>
        <stop offset="1" stop-color="#a8121a"/>
      </linearGradient>
      <linearGradient id="brownFill" x1="0" y1="0" x2="1" y2="0">
        <stop offset="0" stop-color="#2d1a11"/>
        <stop offset="0.5" stop-color="#4a2e1f"/>
        <stop offset="1" stop-color="#2d1a11"/>
      </linearGradient>
    </defs>
    <text transform="translate(640 386) rotate(-90)" font-family="Oswald, sans-serif" font-weight="700" font-size="56" fill="url(#silverFill)" textLength="351" lengthAdjust="spacingAndGlyphs">CELEBRATING</text>
    <text x="660" y="160" font-family="Anton, sans-serif" font-size="145" fill="url(#redFill)" textLength="506" lengthAdjust="spacingAndGlyphs">20 YEARS</text>
    <text x="656" y="288" font-family="Anton, sans-serif" font-size="128" fill="url(#silverFill)" textLength="514" lengthAdjust="spacingAndGlyphs">TOGETHER</text>
    <rect x="653" y="303" width="515" height="81" fill="url(#brownFill)"/>
    <text x="665" y="369" font-family="Anton, sans-serif" font-size="60" fill="#ffffff" textLength="488" lengthAdjust="spacingAndGlyphs">TOWARDS TOMORROW</text>
  </svg>

  <div class="rule" style="top:419px"></div>
  <div class="event-banner">
    <div class="edition">20TH ANNUAL</div>
    <div class="event-name">PLVW CONFERENCE</div>
  </div>
  <div class="rule" style="top:530px"></div>

  <div class="event-date" style="left:598px">
    <svg class="date-art" width="245" height="130" viewBox="0 0 245 130">
      <text x="0" y="28" font-family="Montserrat, sans-serif" font-size="32" letter-spacing="2" fill="#fff" textLength="178" lengthAdjust="spacingAndGlyphs">TUESDAY</text>
      <text x="0" y="115" font-family="Montserrat, sans-serif" font-weight="800" font-size="112" fill="url(#silverFill)" textLength="118" lengthAdjust="spacingAndGlyphs">15</text>
      <text x="122" y="75" font-family="Montserrat, sans-serif" font-weight="800" font-size="46" fill="url(#silverFill)" textLength="68" lengthAdjust="spacingAndGlyphs">TH</text>
      <rect x="124" y="85" width="80" height="30" fill="#6a0f12"/>
      <text x="130" y="111" font-family="Montserrat, sans-serif" font-weight="800" font-size="28" fill="#fff" textLength="68" lengthAdjust="spacingAndGlyphs">MAY</text>
      <text transform="translate(240 116) rotate(-90)" font-family="Montserrat, sans-serif" font-weight="800" font-size="36" fill="#9aa1aa" textLength="114" lengthAdjust="spacingAndGlyphs">2018</text>
    </svg>
    <div class="time">12:30PM - 5:00PM</div>
  </div>

  <div class="date-joiner">&amp;</div>

  <div class="event-date" style="left:921px">
    <svg class="date-art" width="245" height="130" viewBox="0 0 245 130">
      <text x="0" y="28" font-family="Montserrat, sans-serif" font-size="32" letter-spacing="2" fill="#fff" textLength="208" lengthAdjust="spacingAndGlyphs">WEDNESDAY</text>
      <text x="0" y="115" font-family="Montserrat, sans-serif" font-weight="800" font-size="112" fill="url(#silverFill)" textLength="118" lengthAdjust="spacingAndGlyphs">16</text>
      <text x="122" y="75" font-family="Montserrat, sans-serif" font-weight="800" font-size="46" fill="url(#silverFill)" textLength="68" lengthAdjust="spacingAndGlyphs">TH</text>
      <rect x="124" y="85" width="80" height="30" fill="#6a0f12"/>
      <text x="130" y="111" font-family="Montserrat, sans-serif" font-weight="800" font-size="28" fill="#fff" textLength="68" lengthAdjust="spacingAndGlyphs">MAY</text>
      <text transform="translate(240 116) rotate(-90)" font-family="Montserrat, sans-serif" font-weight="800" font-size="36" fill="#9aa1aa" textLength="114" lengthAdjust="spacingAndGlyphs">2018</text>
    </svg>
    <div class="time">7:30AM - 5:30PM</div>
  </div>

  <div class="info-band">
    <svg class="band-shape" width="1200" height="60" viewBox="0 0 1200 60">
      <polygon points="0,0 702,0 680,60 0,60" fill="#3a3b3d"/>
      <polygon points="710,0 1200,0 1200,60 688,60" fill="#b3131c"/>
    </svg>
    <div class="venue">
      <svg width="18" height="26" viewBox="0 0 18 26" aria-hidden="true">
        <path d="M9 1a8 8 0 0 0-8 8c0 6 8 16 8 16s8-10 8-16a8 8 0 0 0-8-8z" fill="none" stroke="#fff" stroke-width="2.5"/>
        <circle cx="9" cy="9" r="3" fill="#fff"/>
      </svg>
      <span>The HALL at the Corvane Manchester</span>
    </div>
    <div class="website">
      <svg width="30" height="30" viewBox="0 0 30 30" aria-hidden="true" fill="none" stroke="#fff" stroke-width="2">
        <circle cx="15" cy="15" r="13"/>
        <ellipse cx="15" cy="15" rx="6" ry="13"/>
        <line x1="2" y1="15" x2="28" y2="15"/>
        <line x1="4" y1="8" x2="26" y2="8"/>
        <line x1="4" y1="22" x2="26" y2="22"/>
      </svg>
      <span>www.plvwsummit.example</span>
    </div>
  </div>
  <div class="card-foot"></div>
</main>
</body>
</html>
```